UI/UX design for non-profit education/student success foundation website

Looking to work with a ui/ux designer that can provide an elegant, impactful and modern responsive design for a non-profit education/student success foundation website. The website will need to have a lot of visuals and elements with impactful statements. The responsive templates will later be parsed (this will be done by another developer) and converted to Concrete5 CMS templates. The organization likes bold colors with a modern sleek design. Typography is also key in titles and statements of interest. On-scroll visuals could be nice if it lends well to combining imagery and text. The site will need templates for a homepage, global sub-page, and contact page. Interchangeable block elements would be nice if we want to create other templates or change element positions.

Target Market(s)

Continued education and philanthropy individuals/organizations

Industry/Entity Type

Non-profit / college education

Coding

Coded - Design and coding required

Number of Pages Required

3 page

Font styles to use
Sans Serif
Script

Colors
0094D4
00A9DD
6FCCEA
C7EBF8
E9F6FB
59FF00
82FF00
B8FF75
E3FFCB
F4FFEA
FFC000
F8CF3A
FAE287
FDF2CF
FEFAEE
EE7325
F08F49
F5BC92
FAE3D3
FDF4ED
6B429C
8869AF
B7A5CE
E3DAEB
F3F0F8

Requirements
Must have
• Modern responsive design, impactful visual elements, available theme elements pre styled for things like forms, buttoms, tables...
Nice to have
• Onscroll vidual effects, heros with background video

```html
<!DOCTYPE html>
<html lang="en">
<head>
<meta charset="utf-8">
<title>The Meridian Foundation</title>
<link href="https://fonts.googleapis.com/css2?family=Poppins:ital,wght@0,400;0,500;0,600;0,700;1,400&family=Yellowtail&display=swap" rel="stylesheet">
<style>
:root{
  --purple:#6B429C;
  --purple-dark:#4a2b73;
  --purple-soft:#8869AF;
  --lavender:#F3F0F8;
  --orange:#EE7325;
  --orange-light:#F08F49;
  --yellow:#FFC000;
  --yellow-soft:#F8CF3A;
  --sky:#E9F6FB;
  --blue:#0094D4;
  --ink:#2a2340;
  --grey:#666;
  --white:#fff;
  --sans:'Poppins',Arial,sans-serif;
  --script:'Yellowtail',cursive;
}
*{margin:0;padding:0;box-sizing:border-box}
html,body{width:1200px;height:5141px;overflow:hidden}
body{font-family:var(--sans);color:var(--ink);position:relative;background:var(--white)}
section,header,footer{position:absolute;left:0;width:1200px;overflow:hidden}
.abs{position:absolute}
.script{font-family:var(--script);font-weight:400}
.btn{position:absolute;display:flex;align-items:center;justify-content:center;border-radius:24px;font-size:12px;font-weight:600;letter-spacing:1.5px;text-transform:uppercase;color:var(--white)}
.center{left:0;width:1200px;text-align:center}

/* hero */
.hero{top:0;height:724px}
.hero-photo{position:absolute;inset:0;background:linear-gradient(120deg,#6d7a86 0%,#4b5560 40%,#7a6d62 70%,#3f4650 100%)}
.hero-shade{position:absolute;inset:0;background:rgba(20,25,40,.35)}
.brand{position:absolute;display:flex;align-items:center;gap:10px}
.brand-square{width:36px;height:36px;background:var(--orange);border-radius:4px}
.brand-name{font-weight:600;font-size:19px;line-height:1.05;text-transform:uppercase;letter-spacing:.5px}
.hero .brand-name{color:var(--white)}
.nav{position:absolute;top:38px;left:430px;display:flex;gap:0}
.nav a{display:block;width:140px;text-align:center;color:var(--white);font-size:11px;font-weight:600;letter-spacing:.6px;text-decoration:none;text-transform:uppercase;position:relative;height:30px}
.nav a.active::after{content:"";position:absolute;left:36px;right:36px;top:26px;height:2px;background:var(--yellow)}
.play{position:absolute;left:580px;top:244px;width:56px;height:56px;border-radius:50%;background:var(--orange)}
.hero h1{position:absolute;top:310px;font-size:40px;font-weight:600;color:var(--white);line-height:45px}
.hero .vision{position:absolute;top:300px;left:0;width:1200px;text-align:center;font-size:74px;color:var(--white);line-height:1;transform:translate(10px,0)}

/* empower */
.empower{top:724px;height:560px;background:linear-gradient(90deg,var(--yellow) 0%,#f9a81a 45%,var(--orange) 100%)}
.empower .script{position:absolute;top:108px;font-size:40px;color:var(--white)}
.empower h2{position:absolute;top:160px;font-size:32px;font-weight:600;color:var(--white)}
.empower p{position:absolute;top:232px;left:290px;width:620px;text-align:center;font-size:14px;line-height:25px;color:var(--white)}
.wave{position:absolute;left:0;top:1180px;width:1200px;height:120px}

/* why */
.why{top:1270px;height:600px;background:var(--purple)}
.why-photo{position:absolute;left:560px;top:0;width:640px;height:600px;background:linear-gradient(90deg,var(--purple) 0%,#7d6a7c 30%,#b89a5a 60%,#d9a73a 100%)}
.why .script{position:absolute;left:154px;top:122px;font-size:38px;color:var(--yellow)}
.why h2{position:absolute;left:154px;top:178px;font-size:30px;font-weight:600;color:var(--white);line-height:37px}
.why h2 span{font-weight:400}
.why p{position:absolute;left:154px;top:266px;width:470px;font-size:15px;line-height:27px;color:#ece4f5}

/* services */
.services{top:1870px;height:772px;background:var(--sky)}
.sec-title{position:absolute;left:0;width:1200px;text-align:center;font-family:var(--script);color:var(--purple);font-size:54px;line-height:1}
.sec-rule{position:absolute;left:583px;width:34px;height:2px;background:var(--purple)}
.card{position:absolute;width:292px;height:232px;background:var(--white);border:1px solid #dfe6ea}
.card .ph{position:absolute;left:6px;top:6px;right:6px;height:172px}
.card span{position:absolute;left:0;right:0;top:190px;text-align:center;font-size:17px;font-weight:500;color:#333}

/* blogs */
.blogs{top:2642px;height:566px;background:var(--white)}
.post{position:absolute;width:304px;height:328px;border:1px solid #d9d9d9;background:var(--white)}
.post .ph{position:absolute;left:0;top:0;width:100%;height:186px}
.post .date{position:absolute;left:22px;top:202px;width:100px;height:22px;background:var(--orange);color:var(--white);font-size:10px;font-weight:600;display:flex;align-items:center;justify-content:center}
.post h3{position:absolute;left:22px;top:236px;width:270px;font-size:13px;font-weight:600;line-height:19px;color:#222}
.post a{position:absolute;left:22px;top:286px;font-size:9px;font-weight:600;color:var(--purple);text-decoration:none;letter-spacing:.5px}

/* testimonials */
.voices{top:3208px;height:482px;background:var(--lavender)}
.quote{position:absolute;top:138px;width:440px;height:240px;border:2px solid var(--orange-light);background:var(--white);text-align:center}
.quote p{position:absolute;left:24px;right:24px;top:96px;font-size:13px;line-height:21px;color:#333}
.quote b{position:absolute;left:0;right:0;top:196px;font-size:15px;font-weight:600;color:#222}
.avatar{position:absolute;width:152px;height:152px;border-radius:50%;border:2px solid var(--yellow-soft);background:#fdf4ed;padding:8px}
.avatar div{width:100%;height:100%;border-radius:50%;background:linear-gradient(135deg,#e8e1d8,#b9b0a6)}

/* feature */
.feature{top:3690px;height:562px;background:var(--purple)}
.feature-photo{position:absolute;left:0;top:0;width:760px;height:562px;background:linear-gradient(90deg,#8a7a70 0%,#a8908a 35%,#7f6e9a 75%,var(--purple) 100%)}
.frame{position:absolute;left:876px;top:108px;width:202px;height:352px;border:2px solid var(--yellow);border-left:none}
.frame::before,.frame::after{content:"";position:absolute;left:0;width:2px;height:30px;background:var(--yellow)}
.frame::before{top:0}.frame::after{bottom:0}
.feature .script{position:absolute;left:672px;top:174px;font-size:48px;line-height:46px;color:var(--white)}
.feature p{position:absolute;left:680px;top:288px;width:400px;font-size:15px;font-style:italic;line-height:29px;color:#efe8f7}

/* support */
.support{top:4252px;height:518px;background:var(--orange)}
.support .script{position:absolute;left:122px;top:132px;font-size:46px;line-height:46px;color:var(--white)}
.support p{position:absolute;left:122px;top:244px;width:400px;font-size:15px;font-style:italic;line-height:29px;color:var(--white)}
.support-photo{position:absolute;left:570px;top:106px;width:478px;height:326px;background:linear-gradient(135deg,#6f7d55 0%,#2c2b34 45%,#b8282d 75%,#3a2f33 100%)}

/* footer */
.footer{top:4770px;height:310px;background:var(--white)}
.footer .brand-name{color:var(--blue)}
.foot-about{position:absolute;left:140px;top:120px;width:220px;font-size:11px;line-height:16px;color:#555}
.col{position:absolute;top:78px}
.col h4{font-size:15px;font-weight:600;color:var(--purple);text-transform:uppercase;letter-spacing:.4px;position:relative;padding-bottom:10px}
.col h4::after{content:"";position:absolute;left:0;bottom:0;width:46px;height:2px;background:var(--orange)}
.col ul{list-style:none;margin-top:14px}
.col li{font-size:12.5px;line-height:25px;color:#555}
.social{display:flex;gap:8px;margin-top:16px}
.social i{display:block;width:32px;height:32px;border-radius:50%;background:var(--blue)}
.copy{position:absolute;left:0;top:5080px;width:1200px;height:61px;background:#f3f3f3;font-size:10px;color:#333;display:flex;align-items:center;justify-content:center}
</style>
</head>
<body>

<header class="hero">
  <div class="hero-photo" role="img" aria-label="Photo of students studying together around a table"></div>
  <div class="hero-shade"></div>
  <div class="brand" style="left:106px;top:24px">
    <i class="brand-square"></i>
    <div class="brand-name">The Meridian<br>Foundation</div>
  </div>
  <nav class="nav">
    <a class="active">Services</a><a>About Us</a><a>Donate</a><a>Education</a><a>Contact</a>
  </nav>
  <div class="play">
    <svg width="56" height="56" viewBox="0 0 56 56"><path d="M24 20 L35 28 L24 36 Z" fill="#fff"/></svg>
  </div>
  <div class="vision script">Our Vision</div>
  <h1 class="center" style="top:384px">We are not giving up on educating<br>the world’s most childrens</h1>
</header>

<section class="empower">
  <div class="abs" style="inset:0;background:linear-gradient(90deg,rgba(255,192,0,.9),rgba(238,115,37,.55))" role="img" aria-label="Faint photo of smiling students"></div>
  <div class="script center">we empower</div>
  <h2 class="center">Education for all childrens</h2>
  <p>Lorem ipsum dolor sit amet, consectetur adipiscing elit, sed do eiusmod tempor incididunt ut labore et dolore magna aliqua. Ut enim ad minim veniam, quis nostrud exercitation ullamco laboris nisi ut aliquip</p>
  <div class="btn" style="left:500px;top:326px;width:168px;height:46px;background:var(--purple)">Learn More</div>
</section>

<section class="why">
  <div class="why-photo" role="img" aria-label="Photo of a smiling student in a yellow sweater writing in a library"></div>
  <div class="script">Why choose us</div>
  <h2>Sed ut perspiciatis unde omnis<br>iste <span>natus error sit voluptatem</span></h2>
  <p>Lorem ipsum dolor sit amet, consectetur piscing elit, sed do eiusmod temporAincididunt ut labore et dolore magna aliqua. Ut enim ad minim aliqua.</p>
  <div class="btn" style="left:154px;top:384px;width:182px;height:46px;background:var(--yellow)">Learn More</div>
</section>

<svg class="wave" viewBox="0 0 1200 120" preserveAspectRatio="none" aria-hidden="true">
  <path d="M0 40 C300 -10 500 90 800 40 C1000 10 1120 40 1200 40 L1200 120 L0 120 Z" fill="#fff"/>
  <path d="M0 56 C300 10 500 100 800 56 C1000 26 1120 56 1200 56 L1200 120 L0 120 Z" fill="#6B429C"/>
  <path d="M0 50 C300 5 500 96 800 50 C1000 20 1120 50 1200 48" fill="none" stroke="#EE7325" stroke-width="3"/>
</svg>

<section class="services">
  <div class="sec-title" style="top:46px">Our Services</div>
  <div class="sec-rule" style="top:112px"></div>
  <div class="card" style="left:148px;top:146px"><div class="ph" role="img" aria-label="Photo of graduates throwing caps" style="background:linear-gradient(135deg,#4f6a3a,#2a2a30)"></div><span>Our History</span></div>
  <div class="card" style="left:462px;top:146px"><div class="ph" role="img" aria-label="Photo of students walking on campus" style="background:linear-gradient(135deg,#d8d3c9,#8a8f9a)"></div><span>Outcomes</span></div>
  <div class="card" style="left:776px;top:146px"><div class="ph" role="img" aria-label="Photo of students on steps with laptops" style="background:linear-gradient(135deg,#8a6f5a,#3f4a66)"></div><span>Others</span></div>
  <div class="card" style="left:148px;top:402px"><div class="ph" role="img" aria-label="Photo of students laughing in a library" style="background:linear-gradient(135deg,#6b5a4a,#3d4a3a)"></div><span>Leadership</span></div>
  <div class="card" style="left:462px;top:402px"><div class="ph" role="img" aria-label="Photo of two graduates in gowns" style="background:linear-gradient(135deg,#556b3e,#1f1f25 50%,#b8282d)"></div><span>Scholarships</span></div>
  <div class="card" style="left:776px;top:402px"><div class="ph" role="img" aria-label="Photo of a student at a laptop" style="background:linear-gradient(135deg,#e9e6e1,#d8a440)"></div><span>Support &amp; help</span></div>
  <div class="btn" style="left:540px;top:668px;width:160px;height:44px;background:var(--orange)">View More</div>
</section>

<section class="blogs">
  <div class="sec-title" style="top:44px">Recent blogs</div>
  <div class="sec-rule" style="top:116px"></div>
  <article class="post" style="left:140px;top:154px"><div class="ph" role="img" aria-label="Photo of students writing in class" style="background:linear-gradient(135deg,#3a3a3a,#bfb9b0)"></div><div class="date">28 MAY 2021</div><h3>Lorem ipsum dolor sit amet, con-sectetur adipiscing elit sed do</h3><a>LEARN MORE →</a></article>
  <article class="post" style="left:456px;top:154px"><div class="ph" role="img" aria-label="Photo of a classroom with a raised hand" style="background:linear-gradient(135deg,#c9c2b5,#7a3a2e)"></div><div class="date">28 MAY 2021</div><h3>Lorem ipsum dolor sit amet, con-sectetur adipiscing elit sed do</h3><a>LEARN MORE →</a></article>
  <article class="post" style="left:770px;top:154px"><div class="ph" role="img" aria-label="Photo of students studying at a table" style="background:linear-gradient(135deg,#8a7060,#b8282d 60%,#5a4a40)"></div><div class="date">28 MAY 2021</div><h3>Lorem ipsum dolor sit amet, con-sectetur adipiscing elit sed do</h3><a>LEARN MORE →</a></article>
</section>

<section class="voices">
  <div class="quote" style="left:156px"><p>Lorem Ipsum is simply dummy text of the printing and typesetting industry. Lorem Ipsum has been the industry's standard dummy text ever since the 1500s, when an unknown printer stry's standard ustry. Lorem Ipsum has been</p><b>By Owen</b></div>
  <div class="quote" style="left:608px"><p>Lorem Ipsum is simply dummy text of the printing and typesetting industry. Lorem Ipsum has been the industry's standard dummy text ever since the 1500s, when an unknown printer stry's standard ustry. Lorem Ipsum has been</p><b>by Dana</b></div>
  <div class="avatar" style="left:292px;top:64px"><div role="img" aria-label="Portrait photo of reviewer"></div></div>
  <div class="avatar" style="left:742px;top:64px"><div role="img" aria-label="Portrait photo of reviewer" style="background:linear-gradient(135deg,#7cc6c9,#4d8c9a)"></div></div>
</section>

<section class="feature">
  <div class="feature-photo" role="img" aria-label="Photo of a student writing at a desk in a library"></div>
  <div class="frame"></div>
  <div class="script">We Empower<br>Education for all</div>
  <p>Lorem Ipsum is simply dummy text of the printing and typesetting industry. Lorem Ipsum has been the industry's standard dummy text ever.</p>
</section>

<section class="support">
  <svg class="abs" style="left:0;top:0" width="1200" height="518" aria-hidden="true">
    <path d="M960 0 L1200 0 L1200 518 L730 518 Z" fill="#FFC000"/>
    <circle cx="620" cy="180" r="96" fill="none" stroke="#fff" stroke-opacity=".7" stroke-width="1.5"/>
    <circle cx="620" cy="180" r="78" fill="none" stroke="#fff" stroke-opacity=".7" stroke-width="1.5"/>
  </svg>
  <div class="script">Education Support<br>is Powerful</div>
  <p>Lorem Ipsum is simply dummy text of the printing and typesetting industry. Lorem Ipsum has been the industry's standard dummy text ever.</p>
  <div class="btn" style="left:122px;top:356px;width:150px;height:40px;background:var(--yellow)">Learn More</div>
  <div class="support-photo" role="img" aria-label="Photo of two smiling graduates in caps and gowns"></div>
</section>

<footer class="footer">
  <div class="brand" style="left:124px;top:66px">
    <i class="brand-square" style="width:40px;height:40px"></i>
    <div class="brand-name" style="font-size:22px">The Meridian<br>Foundation</div>
  </div>
  <p class="foot-about">Lorem ipsum dolor sit amet, consectetur adipiscing elit sed do eiusmod tempor incididunt</p>
  <div class="col" style="left:452px"><h4>Navigation</h4><ul><li>Services</li><li>About Us</li><li>Donate</li><li>Education</li><li>Blogs</li></ul></div>
  <div class="col" style="left:652px"><h4>Resources</h4><ul><li>Upcoming Events</li><li>Why We Are</li><li>Resources</li><li>Support</li><li>Contact Us</li></ul></div>
  <div class="col" style="left:866px"><h4>Follow Us</h4><div class="social"><i></i><i></i><i></i><i></i></div></div>
</footer>
<div class="copy">2021 Copyright © Company Name All Right Reserved</div>

</body>
</html>
```